100% No Money Down

Flyer Design

Used for IG & FB (Social Media) Post. So avoid 8 1/2 x 11.

Target Market(s)

Real Estate Investors

Industry/Entity Type

Mortgage Brokerage

Requirements
Must have
• (LARGE BOLD FONT)
• 100% Investor Financing
• Fix & Flip Joint Ventures
• * Closing Costs Financed
• * 2-3 Week Close
• * No Score Minimum
• * No Reserve Requirement
• Contact: Marcus Delwyn
• Bluegate Lending Partners, Inc.
• NMLS #58307 / #916482
• Direct (240) 555-0193
• Email mdelwyn@bluegatelendpro.com

```html
<!DOCTYPE html>
<html lang="en">
<head>
<meta charset="utf-8">
<title>Fix &amp; Flip Joint Ventures Flyer</title>
<link rel="stylesheet" href="https://fonts.googleapis.com/css2?family=Oswald:wght@300;400;500&family=Roboto+Condensed:wght@300;400;700&display=swap">
<style>
  :root{
    --bg:#bcdcec;
    --navy:#2a2c63;
    --navy-deep:#222456;
    --royal:#3b4594;
    --royal-light:#4a55a6;
    --gold:#d9a94a;
    --white:#ffffff;
    --photo-a:#e6ebe8;
    --photo-b:#b9c2bd;
    --portrait-a:#3e5f86;
    --portrait-b:#1d2233;
  }
  *{box-sizing:border-box;margin:0;padding:0}
  html,body{width:1200px;height:1022px;overflow:hidden}
  body{background:var(--bg);display:flex;align-items:center;justify-content:center;font-family:"Roboto Condensed",Arial,sans-serif;color:var(--white)}
  .flyer{width:440px;height:980px;display:flex;flex-direction:column;background:var(--navy);box-shadow:0 10px 30px rgba(20,40,70,.25)}
  .header{height:130px;background:linear-gradient(180deg,var(--navy-deep),var(--navy));display:flex;flex-direction:column;align-items:center;justify-content:center;text-align:center}
  .header .eyebrow{font-family:"Oswald",sans-serif;font-weight:400;font-size:19px;letter-spacing:.5px}
  .header .title{font-family:"Oswald",sans-serif;font-weight:400;font-size:38px;letter-spacing:.5px;line-height:1.15}
  .rule{height:4px;background:linear-gradient(90deg,#b7832f,var(--gold),#f1cf83,var(--gold))}
  .benefits{height:200px;background:linear-gradient(180deg,var(--royal-light),var(--royal));padding:24px 0 0 48px}
  .benefits .headline{font-family:"Oswald",sans-serif;font-weight:400;font-size:24px;letter-spacing:1.5px;margin-left:-20px;margin-bottom:10px}
  .benefits ul{list-style:none;margin-left:18px}
  .benefits li{display:flex;align-items:center;gap:20px;font-weight:300;font-size:22px;line-height:32px}
  .benefits svg{width:22px;height:22px;flex:none}
  .photo{height:350px;background:radial-gradient(circle at 50% 45%,var(--photo-a),var(--photo-b))}
  .contact{height:233px;display:flex;background:linear-gradient(180deg,var(--navy),var(--navy-deep))}
  .portrait{width:170px;margin-top:80px;background:linear-gradient(160deg,var(--portrait-a),var(--portrait-b))}
  .details{flex:1;padding:22px 14px 0 14px;font-size:12.5px;line-height:1.4}
  .details .label{font-weight:700}
  .details dl{display:grid;grid-template-columns:56px 1fr;margin-top:2px}
  .details dt{font-weight:700}
  .terms{height:63px;background:var(--royal);display:flex;align-items:center;justify-content:space-around;padding:0 10px;font-weight:300;font-size:14px}
</style>
</head>
<body>
  <article class="flyer">
    <header class="header">
      <p class="eyebrow">100% INVESTOR FINANCING</p>
      <h1 class="title">FIX &amp; FLIP JOINT VENTURES</h1>
    </header>
    <div class="rule"></div>
    <section class="benefits">
      <h2 class="headline">ACTUALLY GET MONEY BACK AT CLOSE</h2>
      <ul>
        <li><svg viewBox="0 0 22 22"><circle cx="11" cy="11" r="9.5" fill="none" stroke="#fff" stroke-width="1.3"/><path d="M6.5 11.3l3 3 6-6.2" fill="none" stroke="#fff" stroke-width="1.4"/></svg>Closing Costs Financed</li>
        <li><svg viewBox="0 0 22 22"><circle cx="11" cy="11" r="9.5" fill="none" stroke="#fff" stroke-width="1.3"/><path d="M6.5 11.3l3 3 6-6.2" fill="none" stroke="#fff" stroke-width="1.4"/></svg>2-3 Week Close</li>
        <li><svg viewBox="0 0 22 22"><circle cx="11" cy="11" r="9.5" fill="none" stroke="#fff" stroke-width="1.3"/><path d="M6.5 11.3l3 3 6-6.2" fill="none" stroke="#fff" stroke-width="1.4"/></svg>No Score Minimum</li>
        <li><svg viewBox="0 0 22 22"><circle cx="11" cy="11" r="9.5" fill="none" stroke="#fff" stroke-width="1.3"/><path d="M6.5 11.3l3 3 6-6.2" fill="none" stroke="#fff" stroke-width="1.4"/></svg>No Reserve Requirement</li>
      </ul>
    </section>
    <div class="rule"></div>
    <div class="photo" role="img" aria-label="Photo of a smiling man in a grey suit celebrating as banknotes fall around him"></div>
    <section class="contact">
      <div class="portrait" role="img" aria-label="Portrait photo of the loan officer in a dark suit"></div>
      <div class="details">
        <p class="label">Contact:</p>
        <p>Marcus Delwyn, NMLS #58307, Bluegate Lending Partners, Inc., 4120 Linden Park Way, Suite 210, Bowie, MD 20716, NMLS #916482,</p>
        <dl>
          <dt>Phone</dt><dd>(800) 555-0142 x17, Direct (240) 555-0193</dd>
          <dt>Email</dt><dd>mdelwyn@bluegatelendpro.com</dd>
          <dt>Website</dt><dd>www.bluegatelendpro.com</dd>
        </dl>
      </div>
    </section>
    <footer class="terms">
      <span>Depending on Experience</span>
      <span>Rates 10-12%</span>
      <span>Points 2-4%</span>
      <span>Profit Sharing 35-50%</span>
    </footer>
  </article>
</body>
</html>
```